Holiday Sale 2026 Graphics for New Year

I want to create 10 social media graphics (new Instagram size 4:5 (1080 x 1350 pixels) focusing on our Holiday Sale Graphics, using any of the pics attached. Use the attached pics, NO RANDOM STOCK PHOTOGRAPHY. For the color scheme of the graphics, they should all be complementary to the product colors in the photos.
You can add any of the photos attached but none are required. You can do some of the graphics in all text. I mainly need BOLD text that says one of the headlines with the pics (10 total):
1. 25% OFF Holiday Sale: New You Starts Now!
2. 25% OFF Everything: New Year, New You
3. 25% OFF Christmas Sale 🎁 Feel Amazing Again!
4. Holiday Treat: 25% OFF Your Favorites
5. 25% OFF All Supplements ✨ New Year Reset!
6. Holiday Magic: 25% OFF Every Supplement
7. 25% OFF to Kickstart Your New Year Goals
8. New Year, New Waistline! 25% OFF Sale
9. Holiday Sale: 25% OFF Everything
10. A Better You Begins With 25% OFF

```html
<!DOCTYPE html>
<html lang="en">
<head>
<meta charset="utf-8">
<title>Holiday Sale 2026 — Social Graphics Set</title>
<link href="https://fonts.googleapis.com/css2?family=Oswald:wght@500;600;700&display=swap" rel="stylesheet">
<style>
  :root{
    --backdrop-1:#f4f4f4;
    --backdrop-2:#d9d9d9;
    --pink:#ef5f8b;
    --pink-light:#f8a3bd;
    --wine:#970a24;
    --wine-light:#c81b3d;
    --green:#1d6a3a;
    --green-light:#4c9a66;
    --plum:#962a85;
    --plum-light:#c86db5;
    --red:#e0232b;
    --red-light:#f2787a;
    --ink:#ffffff;
    --counter:#ecebe8;
  }
  *{box-sizing:border-box;margin:0;padding:0}
  html,body{width:1200px;height:600px;overflow:hidden}
  body{
    background:linear-gradient(135deg,var(--backdrop-1),var(--backdrop-2));
    font-family:"Oswald",sans-serif;
    position:relative;
  }
  .post{
    position:absolute;width:194px;height:243px;overflow:hidden;
    background:var(--base);
    box-shadow:3px 5px 8px rgba(0,0,0,.28);
  }
  .post__glow{
    position:absolute;left:62px;top:-40px;width:260px;height:300px;border-radius:50%;
    background:radial-gradient(circle at 60% 30%,var(--light),var(--base) 75%);
  }
  .post__photo{
    position:absolute;left:82px;top:12px;right:0;bottom:0;
    background:
      linear-gradient(180deg,transparent 78%,var(--counter) 78%),
      radial-gradient(ellipse at 50% 35%,rgba(255,255,255,.35),rgba(0,0,0,.15) 70%);
    border-top-left-radius:50px;
  }
  .post__copy{
    position:absolute;left:7px;top:7px;width:74px;
    color:var(--ink);text-transform:uppercase;font-weight:700;line-height:.92;
  }
  .deal{
    border:1.5px solid var(--ink);padding:3px 4px 2px;text-align:center;margin:2px 0 4px;
  }
  .deal__pct{display:block;font-size:31px;font-weight:600}
  .deal__off{display:block;font-size:31px;letter-spacing:6px;margin-right:-6px}
  .deal__tag{display:block;background:var(--ink);color:var(--base);font-size:9px;padding:2px 0 1px;margin:3px -4px -2px}
  .xl{font-size:36px;display:block}
  .lg{font-size:28px;display:block}
  .md{font-size:20px;display:block;font-weight:600}
  .sm{font-size:15px;display:block;font-weight:600}
  .xs{font-size:12px;display:block;font-weight:600}

  .pink{--base:var(--pink);--light:var(--pink-light)}
  .wine{--base:var(--wine);--light:var(--wine-light)}
  .green{--base:var(--green);--light:var(--green-light)}
  .plum{--base:var(--plum);--light:var(--plum-light)}
  .red{--base:var(--red);--light:var(--red-light)}

  .c1{left:78px}.c2{left:290px}.c3{left:503px}.c4{left:715px}.c5{left:928px}
  .r1{top:48px}.r2{top:309px}
</style>
</head>
<body>

<section class="post pink c1 r1">
  <div class="post__glow"></div>
  <div class="post__photo" role="img" aria-label="Smiling woman in white sweater presenting supplement bottles on a marble counter"></div>
  <div class="post__copy">
    <div class="deal"><span class="deal__pct">25%</span><span class="deal__off">OFF</span></div>
    <span class="md">Holiday</span><span class="xl">Sale</span><span class="md">New You</span><span class="sm">Starts Now!</span>
  </div>
</section>

<section class="post wine c2 r1">
  <div class="post__glow"></div>
  <div class="post__photo" role="img" aria-label="Woman in sheer black top gesturing toward supplement bottles"></div>
  <div class="post__copy">
    <div class="deal"><span class="deal__pct">25%</span><span class="deal__off">OFF</span><span class="deal__tag" style="font-size:12px">Everything</span></div>
    <span class="md">New Year</span><span class="md">New You</span>
  </div>
</section>

<section class="post green c3 r1">
  <div class="post__glow"></div>
  <div class="post__photo" role="img" aria-label="Smiling woman in white sweater with row of supplement bottles"></div>
  <div class="post__copy">
    <div class="deal"><span class="deal__pct">25%</span><span class="deal__off">OFF</span></div>
    <span class="sm">Christmas</span><span class="xl">Sale</span><span class="xs">Feel Amazing</span><span class="lg">Again!</span>
  </div>
</section>

<section class="post plum c4 r1">
  <div class="post__glow"></div>
  <div class="post__photo" role="img" aria-label="Woman in sheer black top presenting supplement bottles"></div>
  <div class="post__copy">
    <span class="md">Holiday</span><span class="lg">Treat</span>
    <div class="deal"><span class="deal__pct">25%</span><span class="deal__off">OFF</span></div>
    <span class="xl">Your</span><span class="sm">Favorites</span>
  </div>
</section>

<section class="post red c5 r1">
  <div class="post__glow"></div>
  <div class="post__photo" role="img" aria-label="Smiling woman in white sweater pointing at supplement bottles"></div>
  <div class="post__copy">
    <div class="deal"><span class="deal__pct">25%</span><span class="deal__off">OFF</span><span class="deal__tag">All Supplements</span></div>
    <span class="lg">New</span><span class="lg">Year</span><span class="lg">Reset!</span>
  </div>
</section>

<section class="post wine c1 r2">
  <div class="post__glow"></div>
  <div class="post__photo" role="img" aria-label="Woman in sheer black top with supplement bottles on counter"></div>
  <div class="post__copy">
    <span class="md">Holiday</span><span class="lg">Magic</span>
    <div class="deal"><span class="deal__pct">25%</span><span class="deal__off">OFF</span></div>
    <span class="lg">Every</span><span class="sm">Supplement</span>
  </div>
</section>

<section class="post plum c2 r2">
  <div class="post__glow"></div>
  <div class="post__photo" role="img" aria-label="Smiling woman in white sweater behind supplement bottles"></div>
  <div class="post__copy">
    <div class="deal"><span class="deal__pct">25%</span><span class="deal__off">OFF</span></div>
    <span class="xs">To Kickstart</span><span class="lg">Your</span><span class="md">New Year</span><span class="lg">Goals</span>
  </div>
</section>

<section class="post red c3 r2">
  <div class="post__glow"></div>
  <div class="post__photo" role="img" aria-label="Woman in sheer black top presenting supplement bottles"></div>
  <div class="post__copy">
    <span class="md">New Year</span><span class="xl">New</span><span class="md">Waistline</span>
    <div class="deal"><span class="deal__pct">25%</span><span class="deal__off">OFF</span></div>
    <span class="xl">Sale</span>
  </div>
</section>

<section class="post pink c4 r2">
  <div class="post__glow"></div>
  <div class="post__photo" role="img" aria-label="Smiling woman in white sweater with supplement bottles"></div>
  <div class="post__copy">
    <span class="md">Holiday</span><span class="xl">Sale</span>
    <div class="deal"><span class="deal__pct">25%</span><span class="deal__off">OFF</span><span class="deal__tag" style="font-size:12px">Everything</span></div>
  </div>
</section>

<section class="post green c5 r2">
  <div class="post__glow"></div>
  <div class="post__photo" role="img" aria-label="Woman in sheer black top gesturing at supplement bottles"></div>
  <div class="post__copy">
    <span class="md">A Better</span><span class="xl">You</span><span class="sm">Begins With</span>
    <div class="deal"><span class="deal__pct">25%</span><span class="deal__off">OFF</span></div>
  </div>
</section>

</body>
</html>
```